"Dario Quillon" Business Card

Friends

My name is "Dario Quillon" and I need your help! I need a new business card for my personal use.

As background, "Dario Quillon" is actually an alias that I use when I meet women. Please use your creative skills to create an amazing business card for me to use!

In addition to including my name and contact details (see the "Must Have" section), you may wish to add a catchphrase or a title if you think it would help me :)

For background, please see:

http://www.dailybrightwire.com/2013/07/23/morton-feld-dario-quillon_n_5129847.html

Looking forward to seeing what you can do for me.

Hugs and kisses,

Dario Quillon [courtesy of PixelHarbor]

Target Market(s)

Adult women in New York City...or anywhere really.

Industry/Entity Type

Business

Requirements
Must have
• Please include the following details:

Dario Quillon
P: +1-555-3QUILLN
E: secrets@darioquillon-mail.com
Nice to have
• You might include a catchphrase, like "Quillon is my surname But you can call me Mr Smoothstep".

Or perhaps a title, like "Dario Quillon, Head of Sexy Times".

You're creative...I will leave the details to you my friends.
Should not have
• Any references to my actual name...because then, what's the point in using an alias?

```html
<!DOCTYPE html>
<html lang="en">
<head>
<meta charset="utf-8">
<title>Dario Quillon — Business Card</title>
<link rel="stylesheet" href="https://fonts.googleapis.com/css2?family=Great+Vibes&family=Tinos&display=swap">
<style>
  :root {
    --backdrop: #f2f2f2;
    --card-black: #0b0b0b;
    --card-glow: #2a2a2a;
    --ink-white: #ffffff;
    --accent-red: #c0272d;
    --watermark: rgba(255, 255, 255, 0.06);
    --script: "Great Vibes", cursive;
    --serif: "Tinos", "Times New Roman", serif;
  }

  * { margin: 0; padding: 0; box-sizing: border-box; }

  html, body {
    width: 1200px;
    height: 900px;
    overflow: hidden;
    background: var(--backdrop);
  }

  .business-card {
    position: absolute;
    left: 110px;
    top: 170px;
    width: 980px;
    height: 560px;
    border-radius: 36px;
    overflow: hidden;
    background:
      radial-gradient(ellipse 60% 55% at 52% 38%, var(--card-glow) 0%, rgba(42,42,42,0) 70%),
      var(--card-black);
    color: var(--ink-white);
  }

  .watermark-name {
    position: absolute;
    left: 330px;
    top: 40px;
    font-family: var(--script);
    font-size: 330px;
    line-height: 1;
    color: var(--watermark);
    white-space: nowrap;
    transform: rotate(-8deg);
    pointer-events: none;
  }

  .card-name {
    position: absolute;
    left: 0;
    right: 0;
    top: 105px;
    text-align: center;
    font-family: var(--script);
    font-size: 118px;
    font-weight: 400;
    line-height: 1.1;
    white-space: nowrap;
  }

  .card-name .surname { color: var(--accent-red); }

  .catchphrase {
    position: absolute;
    left: 0;
    right: 0;
    top: 282px;
    text-align: center;
    font-family: var(--serif);
    font-size: 25px;
    color: var(--ink-white);
    white-space: nowrap;
  }

  .catchphrase .highlight { color: var(--accent-red); }

  .contact-list {
    position: absolute;
    left: 70px;
    top: 400px;
    list-style: none;
    font-family: var(--serif);
    font-size: 34px;
    color: var(--ink-white);
  }

  .contact-item {
    display: flex;
    align-items: center;
    height: 54px;
  }

  .contact-icon {
    width: 38px;
    height: 30px;
    margin-right: 16px;
    flex: none;
  }
</style>
</head>
<body>
  <article class="business-card">
    <div class="watermark-name" aria-hidden="true">Quillon</div>

    <h1 class="card-name">Dario <span class="surname">Quillon</span></h1>

    <p class="catchphrase">"<span class="highlight">Quillon</span> is my surname But you can call me <span class="highlight">Mr Smoothstep</span>"</p>

    <ul class="contact-list">
      <li class="contact-item">
        <svg class="contact-icon" viewBox="0 0 38 30" aria-hidden="true">
          <path d="M3 10 Q19 0 35 10 L32 15 L26 13 L25 9 Q19 7 13 9 L12 13 L6 15 Z" fill="var(--accent-red)"/>
          <path d="M11 13 L27 13 L33 27 L5 27 Z" fill="var(--accent-red)"/>
          <circle cx="19" cy="20" r="4" fill="var(--card-black)"/>
        </svg>
        <span class="contact-phone">+1-555-3QUILLN</span>
      </li>
      <li class="contact-item">
        <svg class="contact-icon" viewBox="0 0 38 30" aria-hidden="true">
          <rect x="2" y="5" width="34" height="22" fill="none" stroke="var(--accent-red)" stroke-width="2.5"/>
          <path d="M2 5 L19 18 L36 5" fill="none" stroke="var(--accent-red)" stroke-width="2.5"/>
        </svg>
        <span class="contact-email">secrets@darioquillon-mail.com</span>
      </li>
    </ul>
  </article>
</body>
</html>
```